Stonelynk Business Card Design

The Stonelynk Co is an aggregate (crushing) equipment dealer serving Western Canadian provinces. Stonelynk is a distributor of aggregate equipment for different manufacturers.

We are looking to change and update the existing business card which has been used since the existence of the company. A copy of existing card has been attached for reference. The Stonelynk Co logo we want to remain the same and we want the green color to remain the same.

We are wanting something new with a different look. A refreshing card to show a new modern and updated look. No longer wanting to have the manufacturers on the back of the card but something more like our logo on the back of the card with a statement like "Crushing Solutions"

ideas could be:
- card can be different colors on front and back
- front or reverse of the card could possibly be the green color with the logo in black

Target Market(s)

Owners of Aggregate/Crushing companies

Requirements
Must have
• - logo to remain same along with same font within logo
• - green color to remain same
Nice to have
• as noted above under project description
Should not have

```html
<!DOCTYPE html>
<html lang="en">
<head>
<meta charset="utf-8">
<title>Stonelynk Co Business Card</title>
<link rel="stylesheet" href="https://fonts.googleapis.com/css2?family=Archivo:wght@400;500;700;800&display=swap">
<style>
  :root {
    --olive: #7f8000;
    --olive-dark: #6b6c00;
    --ink: #1a1619;
    --paper: #ffffff;
    --backdrop: #3a3a3a;
    --text: #1c1c1c;
  }
  * { box-sizing: border-box; margin: 0; padding: 0; }
  html, body { width: 1200px; height: 900px; overflow: hidden; }
  body {
    background: var(--backdrop);
    font-family: "Archivo", Arial, sans-serif;
    position: relative;
  }
  .card {
    position: absolute;
    left: 270px;
    width: 660px;
    height: 378px;
    border-radius: 28px;
    overflow: hidden;
  }
  .card-front { top: 52px; background: var(--paper); }
  .card-back { top: 470px; background: var(--paper); color: var(--text); }

  .front-art {
    position: absolute; inset: 0;
    background: linear-gradient(165deg, var(--paper) 0%, var(--paper) 22%, var(--olive) 22%, var(--olive) 55%, var(--ink) 55%, var(--ink) 100%);
  }
  .front-name {
    position: absolute;
    top: 34px; right: 40px;
    background: var(--olive);
    color: var(--paper);
    font-weight: 700;
    font-size: 17px;
    letter-spacing: 0.5px;
    padding: 16px 34px;
    border-radius: 50%;
  }

  .brand {
    position: absolute;
    left: 52px; top: 150px;
    display: flex; align-items: center; gap: 14px;
  }
  .brand-dot { width: 22px; height: 22px; border-radius: 50%; background: var(--olive); }
  .brand-name { font-weight: 800; font-size: 24px; color: var(--ink); letter-spacing: 0.3px; }

  .divider {
    position: absolute;
    left: 352px; top: 44px;
    width: 7px; height: 210px;
    border-left: 2px solid var(--olive);
    border-right: 2px solid var(--olive);
  }
  .contact {
    position: absolute;
    left: 390px; top: 44px;
    font-size: 14px; line-height: 1.25;
  }
  .contact-name {
    color: var(--olive);
    font-weight: 700;
    font-size: 19px;
    margin-bottom: 8px;
  }
  .contact-group { margin-bottom: 9px; }
  .contact-row { display: flex; align-items: flex-start; gap: 8px; }
  .contact-row svg { flex: none; margin-top: 1px; }
  .tagline {
    position: absolute;
    left: 0; right: 0; bottom: 40px;
    text-align: center;
    color: var(--olive);
    font-size: 21px;
    letter-spacing: 6px;
    font-weight: 500;
  }
</style>
</head>
<body>

<section class="card card-front">
  <div class="front-art" role="img" aria-label="Abstract organic shapes in olive green, white and black"></div>
  <div class="front-name">THE STONELYNK CO.</div>
</section>

<section class="card card-back">
  <div class="brand">
    <span class="brand-dot"></span>
    <span class="brand-name">THE STONELYNK CO.</span>
  </div>

  <div class="divider"></div>

  <div class="contact">
    <p class="contact-name">DALE MORROW</p>
    <div class="contact-group">
      <div class="contact-row">
        <svg width="14" height="14" viewBox="0 0 14 14"><circle cx="7" cy="7" r="6.5" fill="var(--olive)"/><rect x="5" y="3.5" width="4" height="7" rx="1" fill="none" stroke="#fff" stroke-width="1"/></svg>
        <span>780 555 0142</span>
      </div>
      <div class="contact-row">
        <svg width="14" height="14" viewBox="0 0 14 14"><circle cx="7" cy="7" r="6.5" fill="var(--olive)"/><path d="M4 6 Q7 3 10 6 L9 8 H5 Z" fill="#fff"/></svg>
        <span>780 555 0187</span>
      </div>
      <div class="contact-row">
        <svg width="14" height="14" viewBox="0 0 14 14"><circle cx="7" cy="7" r="6.5" fill="var(--olive)"/><rect x="4" y="5" width="6" height="5" fill="#fff"/></svg>
        <span>780 555 0163</span>
      </div>
    </div>
    <div class="contact-group">
      <div class="contact-row">
        <svg width="14" height="14" viewBox="0 0 14 14"><circle cx="7" cy="7" r="6.5" fill="var(--olive)"/><rect x="3.8" y="4.8" width="6.4" height="4.4" fill="none" stroke="#fff" stroke-width="1"/><path d="M3.8 4.8 L7 7.3 L10.2 4.8" fill="none" stroke="#fff" stroke-width="1"/></svg>
        <span>dale@stonelynk.com</span>
      </div>
      <div class="contact-row">
        <svg width="14" height="14" viewBox="0 0 14 14"><circle cx="7" cy="7" r="6.5" fill="var(--olive)"/><circle cx="7" cy="7" r="3.2" fill="none" stroke="#fff" stroke-width="1"/><path d="M3.8 7 H10.2 M7 3.8 V10.2" stroke="#fff" stroke-width="0.8"/></svg>
        <span>www.stonelynk.ca</span>
      </div>
    </div>
    <div class="contact-group">
      <div class="contact-row">
        <svg width="14" height="14" viewBox="0 0 14 14"><circle cx="7" cy="7" r="6.5" fill="var(--olive)"/><path d="M7 11 C5 8.5 4.5 7.5 4.5 6 A2.5 2.5 0 0 1 9.5 6 C9.5 7.5 9 8.5 7 11 Z" fill="#fff"/><circle cx="7" cy="6" r="0.9" fill="var(--olive)"/></svg>
        <span>5218 - 71B Avenue<br>Redwater, Alberta T0A 2W0</span>
      </div>
    </div>
  </div>

  <p class="tagline">SCREENERS &nbsp;|&nbsp; CRUSHERS &nbsp;|&nbsp; STACKERS</p>
</section>

</body>
</html>
```